Two documents one design language.

We are a small insurance broker who is committed to being open and transparent as possible with our customers.

For years, we have used plain word documents (see attachments) for our Policy Wording and our Terms of Business.

But now think we can do better and these plain documents are falling behind what our competitors are offering.

So we are now looking for both these documents to be professionally designed using the same design language for both.

We are putting few constraints on the design, but we do have some:
- It must be done in word as the wording can be changed at any time, so we must be able to maintain the documents ourselves.
- Any pictures or graphics you use must be royalty free so we can re-produce with any complications.
- Any pictures or graphics you use must been supplied as part of the package.
- You MUST NOT change any wording or grammar, it's not ours to change, its the insurers wording and HAS to be agreed with them.
- You must not split any any paragraph or bullet point over two pages.
- We are an insurance broker so what ever design you use, must look professional and inspire confidence... I.e. if you read it your thoughts turn to, these people are approachable, know what they are doing and will look after me.
- We specialise in musical instrument insurance, so we are looking for musical theming.

```html
<!DOCTYPE html>
<html lang="en">
<head>
<meta charset="utf-8">
<title>Policy Wording – Hartley Bell Insurance Services</title>
<link rel="stylesheet" href="https://fonts.googleapis.com/css2?family=Montserrat:wght@700;800;900&family=Roboto:wght@400;500&display=swap">
<style>
:root{
  --backdrop:#a3a3a3;
  --paper:#f8f2e6;
  --paper-top:#f5eddd;
  --rose:#e9839f;
  --rose-band:#e48fa6;
  --ink:#2b2b2b;
  --body:#3a3a3a;
  --slate:#5a5a5a;
  --white:#ffffff;
}
*{margin:0;padding:0;box-sizing:border-box}
html,body{width:1200px;height:3955px;overflow:hidden}
body{background:var(--backdrop);position:relative;font-family:'Roboto',sans-serif;color:var(--body)}
.page{position:absolute;left:155px;width:890px;height:1150px;background:var(--paper);overflow:hidden;box-shadow:0 10px 30px rgba(0,0,0,.35)}
.cover{top:196px}
.definitions{top:1403px}
.contents{top:2607px}

/* cover */
.cover-head{position:absolute;left:0;top:0;width:890px;height:211px;background:var(--paper-top);display:flex;flex-direction:column;align-items:center;justify-content:center}
.brand-name{font-family:'Montserrat',sans-serif;font-weight:800;color:var(--ink);font-size:40px;letter-spacing:1px;line-height:1.1;text-align:center}
.cover-band{position:absolute;left:0;top:211px;width:890px;height:84px;background:var(--rose-band);display:flex;align-items:center;justify-content:center}
.cover-title{font-family:'Montserrat',sans-serif;font-weight:800;font-size:62px;color:var(--white);letter-spacing:1px}
.cover-photo{position:absolute;left:0;top:295px;width:890px;height:855px;background:linear-gradient(180deg,#4a4a36 0%,#6a6a4a 35%,#8c8a6a 60%,#c9b9a6 80%,#e8a9a6 100%)}

/* inner pages */
.side-wave,.foot-curve{position:absolute;left:0;top:0}
.page-no{position:absolute;right:24px;bottom:8px;font-family:'Montserrat',sans-serif;font-weight:700;font-size:17px;color:var(--white)}
.page-title{position:absolute;top:58px;font-family:'Montserrat',sans-serif;font-weight:900;font-size:58px;color:var(--ink);letter-spacing:.5px}

.definitions .page-title{left:118px}
.def-intro{position:absolute;left:120px;top:133px;font-size:20px;line-height:34px;color:var(--body)}
.def-list{position:absolute;left:120px;top:218px;width:760px}
.def-term{font-size:18px;line-height:28px;font-weight:500;color:var(--rose)}
.def-text{font-size:16.5px;line-height:28px;color:var(--body);margin-bottom:14px}

.contents .page-title{left:132px}
.toc{position:absolute;left:140px;top:155px;width:700px;list-style:none}
.toc li{position:relative;height:57.2px;font-size:19.5px;line-height:30px;color:var(--ink);white-space:nowrap}
.toc-num{position:absolute;left:646px;top:8px;width:34px;height:34px;border-radius:50%;background:var(--rose);color:var(--white);font-size:14px;font-weight:500;display:flex;align-items:center;justify-content:center}
</style>
</head>
<body>

<section class="page cover">
  <header class="cover-head">
    <div class="brand-name">HARTLEY BELL<br>INSURANCE</div>
  </header>
  <div class="cover-band"><h1 class="cover-title">POLICY WORDING</h1></div>
  <div class="cover-photo" role="img" aria-label="Photograph of a harpist playing a golden concert harp on a forest path with pink smoke"></div>
</section>

<section class="page definitions">
  <svg class="side-wave" width="890" height="1150" viewBox="0 0 890 1150" aria-hidden="true">
    <path d="M0 0H84C42 260 38 520 58 720C74 900 82 1040 84 1150H0Z" fill="var(--rose)"/>
  </svg>
  <svg class="foot-curve" width="890" height="1150" viewBox="0 0 890 1150" aria-hidden="true">
    <path d="M390 1150C520 1112 700 1108 890 1110V1150Z" fill="var(--slate)"/>
  </svg>
  <h2 class="page-title">DEFINITIONS</h2>
  <p class="def-intro">Wherever the following words appear in CAPITALS in this policy<br>document they will have the meanings shown below</p>
  <dl class="def-list">
    <dt class="def-term">ENDORSEMENT(S)</dt>
    <dd class="def-text">Any variations or additions to the terms of this insurance.</dd>
    <dt class="def-term">PERIOD OF INSURANCE</dt>
    <dd class="def-text">The length of time for which this insurance is in force as shown in the SCHEDULE, or until cancelled.</dd>
    <dt class="def-term">PREMISES</dt>
    <dd class="def-text">The location stated in the SCHEDULE where the INSURED PROPERTY<br>is usually kept.</dd>
    <dt class="def-term">PROPERTY INSURED</dt>
    <dd class="def-text">The musical instrument(s), equipment and accessories as detailed in the SCHEDULE.</dd>
    <dt class="def-term">SCHEDULE</dt>
    <dd class="def-text">The SCHEDULE is part of the policy.&nbsp; It shows details of YOU, the PROPERTY INSURED,<br>the sums insured, the level of cover, the PERIOD OF INSURANCE and the sections<br>of this insurance which apply.</dd>
    <dt class="def-term">WE/OUR/US</dt>
    <dd class="def-text">a) Northmere Insurance UK Ltd<br>b) Kestrel Underwriting Limited at all times as authorised underwriting agents<br>and administrators (and for no other purpose) for Alder UK Speciality on behlaf<br>of Northmere Insurance UK Ltd with no liability under this Policy<br>c) Hartley Bell Insurance Services as administrators under this policy.</dd>
    <dt class="def-term">YOU/YOUR</dt>
    <dd class="def-text">The person(s) named as the Insured in the SCHEDULE and members of YOUR immediate family.</dd>
    <dt class="def-term">FRIEND</dt>
    <dd class="def-text">A third party whome YOU entrust the PROPERTY INSURED who may transport/use/store<br>in YOUR absense and for which YOU do not receive any commerical reward.</dd>
    <dt class="def-term">TEACHER</dt>
    <dd class="def-text">The person who YOU regually receive instruction on the use of the PROPERTY<br>INSURED and is suitably qualified.</dd>
  </dl>
  <span class="page-no">03</span>
</section>

<section class="page contents">
  <svg class="side-wave" width="890" height="1150" viewBox="0 0 890 1150" aria-hidden="true">
    <path d="M0 0H84C42 260 38 520 58 720C74 900 82 1040 84 1150H0Z" fill="var(--rose)"/>
  </svg>
  <svg class="foot-curve" width="890" height="1150" viewBox="0 0 890 1150" aria-hidden="true">
    <path d="M390 1150C520 1112 700 1108 890 1110V1150Z" fill="var(--slate)"/>
  </svg>
  <h2 class="page-title">CONTENTS</h2>
  <ol class="toc">
    <li>DEFINITIONS<span class="toc-num">02</span></li>
    <li>POLICY OVERVIEW<span class="toc-num">03</span></li>
    <li>CERTIFICATE OF INSURANCE (Public Liability)<span class="toc-num">04</span></li>
    <li>CERTIFICATE OF INSURANCE (Musical Instruments and accessories)<span class="toc-num">06</span></li>
    <li>SCHEDULE<span class="toc-num">08</span></li>
    <li>INFORMATION YOU HAVE GIVEN US<span class="toc-num">09</span></li>
    <li>YOUR DUTIES<span class="toc-num">10</span></li>
    <li>THE COVER PROVIDED<span class="toc-num">11</span></li>
    <li>PUBLIC LIABILITY COVER<span class="toc-num">13</span></li>
    <li>EXCLUSIONS<span class="toc-num">15</span></li>
    <li>HOW TO AMEND YOUR POLICY<span class="toc-num">23</span></li>
    <li>RENEWING YOUR POLICY<span class="toc-num">23</span></li>
    <li>HOW TO CANCEL YOUR POLICY<span class="toc-num">24</span></li>
    <li>CLAIMS CONDITIONS<span class="toc-num">26</span></li>
    <li>HOW TO MAKE A COMPLIANT<span class="toc-num">29</span></li>
    <li>AUTHORISATION &amp; REGULATION<span class="toc-num">32</span></li>
    <li>PRIVICY NOTICES<span class="toc-num">33</span></li>
  </ol>
  <span class="page-no">02</span>
</section>

</body>
</html>
```